IT Company Business Card Rebranding

We want to modernize our business cards massively. We want to incorporate aspects of our old business card such as the white and geometric design with the blues of another icon. Existing Logo, old business card and icon are all attached.

We are a modern IT company that provides support for new and growing technologies and want our business cards to be modern yet professional.
Updates

Note: Do not use file ICON.png in design. This is just a design we like Added Wednesday, March 9, 2016

Industry/Entity Type

Information Technology

Contact Information for Business Card

Roughly 43 : 26 or 1075 x 650 px

Font styles to use
Serif

Colors
0492cd
3276b5
33a6d7
86cfc6
cfeae6
cee9f5
ffffff

Requirements
Must have
• Modern yet professional
Nice to have
• We would like to incorporate the blues of our existing logo and of the icon provided. Really like the design of the icon.
Should not have
• Too Decorative. Just simple and professional.
• Not have the circle icon, as it is a copyrighted icon, I just like the colors and the geometric design

```html
<!DOCTYPE html>
<html lang="en">
<head>
<meta charset="utf-8">
<title>Nexacore IT – Business Card</title>
<link href="https://fonts.googleapis.com/css2?family=Open+Sans:wght@400;600;700;800&display=swap" rel="stylesheet">
<style>
  :root {
    --stage: #e9ebee;
    --paper: #ffffff;
    --paper-shade: #f3f4f6;
    --blue-deep: #1f55b0;
    --blue-mid: #3276b5;
    --blue-bright: #0492cd;
    --blue-sky: #33a6d7;
    --teal: #1aa6c4;
    --ink-grey: #6d7178;
    --white: #ffffff;
  }
  * { box-sizing: border-box; margin: 0; padding: 0; }
  html, body { width: 1200px; height: 800px; overflow: hidden; }
  body {
    background: var(--stage);
    font-family: "Open Sans", Arial, sans-serif;
    display: flex;
    align-items: center;
    justify-content: center;
    gap: 40px;
  }
  .card {
    position: relative;
    width: 540px;
    height: 326px;
    background: var(--paper);
    overflow: hidden;
    box-shadow: 0 10px 24px rgba(40, 50, 70, 0.18);
  }
  .card-art { position: absolute; inset: 0; width: 100%; height: 100%; }

  /* Front */
  .front-brand {
    position: absolute;
    left: 36px;
    top: 78px;
    display: flex;
    align-items: center;
    gap: 14px;
  }
  .brand-mark {
    width: 30px;
    height: 30px;
    border-radius: 50%;
    background: var(--blue-deep);
  }
  .brand-name {
    font-weight: 600;
    font-size: 30px;
    letter-spacing: 0.22em;
    color: var(--ink-grey);
    text-transform: uppercase;
  }

  /* Back */
  .back-brand {
    position: absolute;
    left: 28px;
    top: 200px;
    display: flex;
    align-items: center;
    gap: 10px;
  }
  .back-brand .brand-mark { width: 20px; height: 20px; }
  .back-brand .brand-name { font-size: 18px; }

  .contact {
    position: absolute;
    left: 292px;
    top: 56px;
    color: var(--white);
  }
  .contact-name {
    font-weight: 800;
    font-size: 28px;
    line-height: 1;
    letter-spacing: 0.02em;
  }
  .contact-role {
    font-weight: 600;
    font-size: 14px;
    letter-spacing: 0.06em;
    margin-top: 4px;
    padding-bottom: 8px;
    border-bottom: 2px solid var(--white);
    display: inline-block;
  }
  .contact-list { list-style: none; margin-top: 18px; }
  .contact-list li {
    display: flex;
    align-items: center;
    gap: 10px;
    font-size: 14px;
    margin-bottom: 10px;
  }
  .contact-icon {
    width: 20px;
    height: 20px;
    flex: none;
  }
</style>
</head>
<body>

  <section class="card card-front" aria-label="Business card front">
    <svg class="card-art" viewBox="0 0 540 326" preserveAspectRatio="none" aria-hidden="true">
      <defs>
        <linearGradient id="frontBand" x1="0" y1="0" x2="1" y2="0">
          <stop offset="0" stop-color="#1f55b0"/>
          <stop offset="0.6" stop-color="#0492cd"/>
          <stop offset="1" stop-color="#1aa6c4"/>
        </linearGradient>
      </defs>
      <polygon points="0,222 540,136 540,326 0,326" fill="#2a5fb8"/>
      <polygon points="0,260 540,170 540,326 0,326" fill="url(#frontBand)"/>
      <polygon points="0,260 300,210 0,300" fill="#1f55b0" opacity="0.6"/>
      <polygon points="330,326 540,200 540,326" fill="#33a6d7" opacity="0.35"/>
      <polygon points="120,326 250,230 420,326" fill="#3276b5" opacity="0.3"/>
    </svg>
    <div class="front-brand">
      <span class="brand-mark"></span>
      <span class="brand-name">Nexacore IT</span>
    </div>
  </section>

  <section class="card card-back" aria-label="Business card back">
    <svg class="card-art" viewBox="0 0 540 326" preserveAspectRatio="none" aria-hidden="true">
      <defs>
        <linearGradient id="backPanel" x1="0" y1="0" x2="1" y2="1">
          <stop offset="0" stop-color="#1f55b0"/>
          <stop offset="0.55" stop-color="#0492cd"/>
          <stop offset="1" stop-color="#33a6d7"/>
        </linearGradient>
      </defs>
      <polygon points="196,0 540,0 540,326 250,326" fill="#1a4ea6"/>
      <polygon points="212,0 540,0 540,326 264,326" fill="#2a60bb"/>
      <polygon points="228,0 540,0 540,326 278,326" fill="#3276b5"/>
      <polygon points="244,0 540,0 540,326 292,326" fill="url(#backPanel)"/>
      <polygon points="244,0 420,0 292,326" fill="#1f55b0" opacity="0.35"/>
      <polygon points="400,326 540,120 540,326" fill="#33a6d7" opacity="0.35"/>
      <polygon points="460,0 540,0 540,90" fill="#3276b5" opacity="0.4"/>
    </svg>

    <div class="back-brand">
      <span class="brand-mark"></span>
      <span class="brand-name">Nexacore IT</span>
    </div>

    <div class="contact">
      <p class="contact-name">JONAS</p>
      <p class="contact-role">TECHNICAL SERVICES</p>
      <ul class="contact-list">
        <li>
          <svg class="contact-icon" viewBox="0 0 20 20" aria-hidden="true">
            <circle cx="10" cy="10" r="9" fill="#ffffff"/>
            <path d="M7 5.5l1.6 2.2-1 1.2a6 6 0 0 0 3.5 3.5l1.2-1 2.2 1.6-.9 1.6c-3.8-.3-7-3.5-7.3-7.3z" fill="#1f55b0"/>
          </svg>
          <span>xxxxxxxxxxx</span>
        </li>
        <li>
          <svg class="contact-icon" viewBox="0 0 20 20" aria-hidden="true">
            <circle cx="10" cy="10" r="9" fill="#ffffff"/>
            <rect x="5" y="6.5" width="10" height="7" fill="none" stroke="#1f55b0" stroke-width="1.4"/>
            <path d="M5 6.8l5 3.8 5-3.8" fill="none" stroke="#1f55b0" stroke-width="1.4"/>
          </svg>
          <span>hello@nexacore.net</span>
        </li>
        <li>
          <svg class="contact-icon" viewBox="0 0 20 20" aria-hidden="true">
            <circle cx="10" cy="10" r="9" fill="#ffffff"/>
            <circle cx="10" cy="10" r="5" fill="none" stroke="#1f55b0" stroke-width="1.3"/>
            <path d="M5 10h10M10 5c-2.4 3-2.4 7 0 10M10 5c2.4 3 2.4 7 0 10" fill="none" stroke="#1f55b0" stroke-width="1.1"/>
          </svg>
          <span>www.nexacore.net</span>
        </li>
      </ul>
    </div>
  </section>

</body>
</html>
```